Solar installer company needs retractable banner graphic design

We need a design for a retractable banner. If you Google Heronfly HRFL-800 and HRFL-1200 you can see what the popup banner physically looks like.

We need a design that will fit both the 31.5" (80 CM) Wide X 78.5" (200 CM) Tall banner and the 47.25" (120 CM) x 78.5" (200 CM) tall banner. We want the design to work on either of these widths.

Our logo is attached and needs to be on the banner. Also please include our URL www.TarnvaleSolar.com on the banner.

The retractable banner will be placed at a home show. It needs to get attention and draw people in.

It can be informational, but I do not want to overwhelm people. A site that covers benefits well is http://powerbriefly.org/benefits-of-solar-panels/ but it does NOT need to include all of these. The main point we want to get across is that installing solar is very affordable, will save you thousands of dollars, and is cheaper monthly than your current bill!

I am relying on the designer to know how much information to put on a banner of this size at a home show.

We will narrow down on the design an then fine-tune the words of the sales pitch.

Industry/Entity Type

Graphic Design

```html
<!DOCTYPE html>
<html lang="en">
<head>
<meta charset="utf-8">
<title>TarnvaleSolar Retractable Banners</title>
<link href="https://fonts.googleapis.com/css2?family=Quicksand:wght@500&family=Fira+Sans+Condensed:wght@600&family=Montserrat:wght@800&display=swap" rel="stylesheet">
<style>
  :root {
    --page: #ffffff;
    --sky-light: #f2f2f2;
    --sky-mid: #c9c9c9;
    --sky-dark: #8a8a8a;
    --amber: #f6ac16;
    --amber-deep: #e39a0b;
    --leaf: #3f7a2a;
    --leaf-dark: #1f3d15;
    --steel-blue: #2f78c2;
    --brand-blue: #1e7fd8;
    --brand-orange: #f2a11a;
    --icon-blue: #2a52be;
    --icon-green: #3cbf2a;
    --icon-orange: #e0801f;
    --white: #ffffff;
  }
  * { box-sizing: border-box; margin: 0; padding: 0; }
  html, body { width: 1200px; height: 1200px; overflow: hidden; background: var(--page); }
  .stage { position: relative; width: 1200px; height: 1200px; }
  .banner {
    position: absolute; top: 50px; width: 436px; height: 1092px; overflow: hidden;
    box-shadow: 0 4px 10px rgba(0,0,0,0.35);
  }
  .banner--narrow { left: 114px; }
  .banner--wide { left: 641px; }
  .banner__backdrop { position: absolute; inset: 0; width: 100%; height: 100%; }
  .brand { position: absolute; left: 33px; top: 32px; }
  .brand__mark {
    position: absolute; left: 0; top: 0; width: 84px; height: 84px; border-radius: 50%;
    background: var(--brand-blue);
  }
  .brand__name {
    position: absolute; left: 95px; top: 20px; white-space: nowrap;
    font: 500 34px/1 'Quicksand', sans-serif; color: var(--brand-orange);
  }
  .brand__tagline {
    position: absolute; left: 97px; top: 62px; white-space: nowrap;
    font: 500 12px/1 'Quicksand', sans-serif; letter-spacing: 1.3px; color: var(--brand-orange);
  }
  .benefit {
    position: absolute; font: 600 27px/31px 'Fira Sans Condensed', sans-serif;
    color: var(--white); text-shadow: 0 1px 3px rgba(0,0,0,0.45); white-space: nowrap;
  }
  .benefit--save { right: 184px; top: 186px; text-align: right; color: var(--brand-blue); text-shadow: none; }
  .benefit--home { left: 252px; top: 360px; }
  .benefit--costs { left: 150px; top: 555px; }
  .benefit--energy { left: 237px; top: 708px; font-size: 26px; }
  .benefit--performance { left: 79px; top: 911px; }
  .badge {
    position: absolute; width: 96px; height: 96px; border-radius: 50%;
    box-shadow: 0 2px 5px rgba(0,0,0,0.35);
  }
  .badge svg { width: 100%; height: 100%; display: block; }
  .badge--save { left: 266px; top: 162px; background: var(--icon-blue); }
  .badge--home { left: 146px; top: 354px; background: var(--icon-green); }
  .badge--costs { left: 38px; top: 534px; background: var(--icon-orange); }
  .badge--energy { left: 127px; top: 710px; background: var(--icon-green); }
  .badge--performance { left: 254px; top: 891px; background: var(--icon-blue); }
  .site-url {
    position: absolute; left: 0; right: 0; top: 1036px; text-align: center;
    font: 800 27px/1 'Montserrat', sans-serif; color: var(--white);
    text-shadow: 0 1px 3px rgba(0,0,0,0.5);
  }
</style>
</head>
<body>
<main class="stage">

  <section class="banner banner--narrow">
    <svg class="banner__backdrop" viewBox="0 0 436 1092" preserveAspectRatio="none" role="img" aria-label="Photograph of rooftop solar panels under a cloudy sky with a tree, tinted in amber, blue and green diagonal sections">
      <defs>
        <linearGradient id="sky-narrow" x1="0" y1="0" x2="0" y2="1">
          <stop offset="0" stop-color="var(--sky-light)"/>
          <stop offset="0.3" stop-color="var(--sky-mid)"/>
          <stop offset="0.6" stop-color="var(--sky-dark)"/>
        </linearGradient>
        <linearGradient id="leaf-narrow" x1="0" y1="0" x2="0" y2="1">
          <stop offset="0" stop-color="var(--leaf)"/>
          <stop offset="1" stop-color="var(--leaf-dark)"/>
        </linearGradient>
      </defs>
      <rect width="436" height="1092" fill="url(#sky-narrow)"/>
      <polygon points="436,34 436,1092 0,1092 0,705" fill="var(--amber)"/>
      <polygon points="0,420 130,500 0,622" fill="var(--steel-blue)"/>
      <polygon points="0,622 130,500 270,1092 0,1092" fill="url(#leaf-narrow)"/>
    </svg>
    <div class="brand">
      <div class="brand__mark"></div>
      <div class="brand__name">TarnvaleSolar</div>
      <div class="brand__tagline">Residential and Commercial</div>
    </div>
    <div class="badge badge--save"><svg viewBox="0 0 96 96"><circle cx="48" cy="48" r="22" fill="#fff"/><text x="48" y="57" text-anchor="middle" font-family="Montserrat, sans-serif" font-weight="800" font-size="24" fill="var(--icon-blue)">$</text></svg></div>
    <p class="benefit benefit--save">Save Your<br>Dollars</p>
    <div class="badge badge--home"><svg viewBox="0 0 96 96"><polygon points="48,20 76,46 68,46 68,74 28,74 28,46 20,46" fill="#fff"/><text x="48" y="66" text-anchor="middle" font-family="Montserrat, sans-serif" font-weight="800" font-size="22" fill="var(--icon-green)">$</text></svg></div>
    <p class="benefit benefit--home">Increase<br>Your Home<br>Value</p>
    <div class="badge badge--costs"><svg viewBox="0 0 96 96"><path d="M26 40 A24 24 0 0 1 68 30" fill="none" stroke="#fff" stroke-width="5"/><path d="M70 56 A24 24 0 0 1 28 66" fill="none" stroke="#fff" stroke-width="5"/><polygon points="64,22 74,34 62,36" fill="#fff"/><polygon points="32,74 22,62 34,60" fill="#fff"/><text x="48" y="58" text-anchor="middle" font-family="Montserrat, sans-serif" font-weight="800" font-size="30" fill="#fff">$</text></svg></div>
    <p class="benefit benefit--costs">Reduce Your<br>Business Costs</p>
    <div class="badge badge--energy"><svg viewBox="0 0 96 96"><rect x="43" y="18" width="10" height="6" fill="#fff"/><rect x="33" y="24" width="30" height="52" rx="3" fill="none" stroke="#fff" stroke-width="4"/><rect x="38" y="30" width="20" height="6" fill="#fff"/><rect x="38" y="40" width="20" height="6" fill="#fff"/><rect x="38" y="50" width="20" height="6" fill="#fff"/><rect x="38" y="60" width="20" height="6" fill="#fff"/></svg></div>
    <p class="benefit benefit--energy">Increase<br>Energy Security<br>and Reliability</p>
    <div class="badge badge--performance"><svg viewBox="0 0 96 96"><path d="M20 62 A28 28 0 0 1 76 62 Z" fill="none" stroke="#fff" stroke-width="5" stroke-linejoin="round"/><line x1="48" y1="62" x2="58" y2="40" stroke="#fff" stroke-width="4" stroke-linecap="round"/></svg></div>
    <p class="benefit benefit--performance">Guaranteed<br>Performance</p>
    <p class="site-url">www.tarnvalesolar.com</p>
  </section>

  <section class="banner banner--wide">
    <svg class="banner__backdrop" viewBox="0 0 436 1092" preserveAspectRatio="none" role="img" aria-label="Photograph of a large solar panel array against a bright sky, tinted in amber, blue and green diagonal sections">
      <defs>
        <linearGradient id="sky-wide" x1="0" y1="0" x2="0" y2="1">
          <stop offset="0" stop-color="var(--sky-light)"/>
          <stop offset="0.45" stop-color="#e6e6e6"/>
          <stop offset="0.65" stop-color="var(--sky-mid)"/>
        </linearGradient>
        <linearGradient id="leaf-wide" x1="0" y1="0" x2="0" y2="1">
          <stop offset="0" stop-color="var(--leaf)"/>
          <stop offset="1" stop-color="var(--leaf-dark)"/>
        </linearGradient>
        <linearGradient id="amber-wide" x1="1" y1="0" x2="0" y2="1">
          <stop offset="0" stop-color="var(--amber-deep)"/>
          <stop offset="0.5" stop-color="var(--amber)"/>
          <stop offset="1" stop-color="var(--amber-deep)"/>
        </linearGradient>
      </defs>
      <rect width="436" height="1092" fill="url(#sky-wide)"/>
      <polygon points="436,0 436,1092 0,1092 0,720" fill="url(#amber-wide)"/>
      <polygon points="0,440 115,510 0,720" fill="var(--steel-blue)"/>
      <polygon points="0,720 115,510 300,1092 0,1092" fill="url(#leaf-wide)"/>
    </svg>
    <div class="brand">
      <div class="brand__mark"></div>
      <div class="brand__name">TarnvaleSolar</div>
      <div class="brand__tagline">Residential and Commercial</div>
    </div>
    <div class="badge badge--save"><svg viewBox="0 0 96 96"><circle cx="48" cy="48" r="22" fill="#fff"/><text x="48" y="57" text-anchor="middle" font-family="Montserrat, sans-serif" font-weight="800" font-size="24" fill="var(--icon-blue)">$</text></svg></div>
    <p class="benefit benefit--save">Save Your<br>Dollars</p>
    <div class="badge badge--home"><svg viewBox="0 0 96 96"><polygon points="48,20 76,46 68,46 68,74 28,74 28,46 20,46" fill="#fff"/><text x="48" y="66" text-anchor="middle" font-family="Montserrat, sans-serif" font-weight="800" font-size="22" fill="var(--icon-green)">$</text></svg></div>
    <p class="benefit benefit--home">Increase<br>Your Home<br>Value</p>
    <div class="badge badge--costs"><svg viewBox="0 0 96 96"><path d="M26 40 A24 24 0 0 1 68 30" fill="none" stroke="#fff" stroke-width="5"/><path d="M70 56 A24 24 0 0 1 28 66" fill="none" stroke="#fff" stroke-width="5"/><polygon points="64,22 74,34 62,36" fill="#fff"/><polygon points="32,74 22,62 34,60" fill="#fff"/><text x="48" y="58" text-anchor="middle" font-family="Montserrat, sans-serif" font-weight="800" font-size="30" fill="#fff">$</text></svg></div>
    <p class="benefit benefit--costs">Reduce Your<br>Business Costs</p>
    <div class="badge badge--energy"><svg viewBox="0 0 96 96"><rect x="43" y="18" width="10" height="6" fill="#fff"/><rect x="33" y="24" width="30" height="52" rx="3" fill="none" stroke="#fff" stroke-width="4"/><rect x="38" y="30" width="20" height="6" fill="#fff"/><rect x="38" y="40" width="20" height="6" fill="#fff"/><rect x="38" y="50" width="20" height="6" fill="#fff"/><rect x="38" y="60" width="20" height="6" fill="#fff"/></svg></div>
    <p class="benefit benefit--energy">Increase<br>Energy Security<br>and Reliability</p>
    <div class="badge badge--performance"><svg viewBox="0 0 96 96"><path d="M20 62 A28 28 0 0 1 76 62 Z" fill="none" stroke="#fff" stroke-width="5" stroke-linejoin="round"/><line x1="48" y1="62" x2="58" y2="40" stroke="#fff" stroke-width="4" stroke-linecap="round"/></svg></div>
    <p class="benefit benefit--performance">Guaranteed<br>Performance</p>
    <p class="site-url">www.tarnvalesolar.com</p>
  </section>

</main>
</body>
</html>
```